Looking for updated Letterhead and Compliments Slips to go with our new updated logo. This stationary will be used for letters to suppliers and customers so needs to be practical while also quite classic.

We are an engineering company so needs to be clean and precise

Target Market(s)

SME'S and large automotive customers

Industry/Entity Type

Automotive

Font styles to use
Sans Serif

Colors
85acd3
0356a4
0792cd
33a6d7
85abd2
ffffff

Requirements
Must have
• Address details as below
• KT Fabrications Limited
• Hallmere Road
• Ashbridge
• Northmere
• LP47 9XZ, UK
• Telephone: +44 (0)1632 960418
• Fax: +44 (0)1632 960733
• Email: sales@ktfabrications.example
• Web: www.ktfabrications.example
Nice to have
• Nice to have some element of being a British Manufacturer

```html
<!DOCTYPE html>
<html lang="en">
<head>
<meta charset="utf-8">
<title>KT Fabrications Letterhead</title>
<link href="https://fonts.googleapis.com/css2?family=Montserrat:wght@500&family=Questrial&display=swap" rel="stylesheet">
<style>
  :root {
    --navy: #0356a4;
    --mid-blue: #0792cd;
    --sky-blue: #33a6d7;
    --pale-blue: #85acd3;
    --ink: #2f3338;
    --watermark: #d9e0ea;
    --paper: #ffffff;
  }
  * { margin: 0; padding: 0; box-sizing: border-box; }
  html, body {
    width: 1200px; height: 1200px; overflow: hidden;
    background: var(--paper);
  }
  .letterhead {
    position: absolute; left: 237px; top: 130px;
    width: 726px; height: 940px;
    background: var(--paper);
    box-shadow: 0 0 14px rgba(0,0,0,0.22);
    overflow: hidden;
  }
  .letterhead__art {
    position: absolute; inset: 0; width: 726px; height: 940px;
  }
  .brand-corner {
    position: absolute; left: 40px; top: 72px; width: 130px;
    font-family: "Montserrat", sans-serif; font-weight: 500;
    font-size: 19px; line-height: 1.2; color: var(--ink);
    text-align: center;
  }
  .brand-wordmark {
    position: absolute; right: 51px; top: 84px;
    font-family: "Montserrat", sans-serif; font-weight: 500;
    font-size: 25px; letter-spacing: 0.28em; color: var(--navy);
    white-space: nowrap;
  }
  .brand-watermark {
    position: absolute; left: 0; right: 0; top: 482px;
    text-align: center;
    font-family: "Montserrat", sans-serif; font-weight: 500;
    font-size: 36px; letter-spacing: 0.3em; color: var(--watermark);
    white-space: nowrap;
  }
  .footer-address, .footer-contact {
    position: absolute; top: 824px;
    font-family: "Questrial", sans-serif;
    font-size: 16.5px; line-height: 19.6px; color: var(--paper);
    list-style: none;
  }
  .footer-address { left: 30px; }
  .footer-contact { right: 47px; text-align: right; top: 826px; }
  .footer-contact li { display: flex; justify-content: flex-end; align-items: center; gap: 5px; }
  .footer-contact svg { width: 12px; height: 12px; flex: none; }
</style>
</head>
<body>
  <main class="letterhead">
    <svg class="letterhead__art" viewBox="0 0 908 1175" preserveAspectRatio="none" aria-hidden="true">
      <path class="swoosh swoosh--light" d="M332,0 L420,0 Q330,205 0,258 Q250,200 332,0 Z" fill="var(--sky-blue)"/>
      <path class="swoosh swoosh--mid" d="M370,0 L440,0 Q350,215 0,258 Q285,210 370,0 Z" fill="var(--mid-blue)"/>
      <rect class="header-stripe" x="420" y="45" width="488" height="11" fill="var(--mid-blue)"/>
      <rect class="header-stripe" x="412" y="56" width="496" height="13" fill="var(--sky-blue)"/>
      <path class="swoosh swoosh--dark" d="M414,0 L908,0 L908,45 L430,45 Q330,232 0,258 Q310,222 414,0 Z" fill="var(--navy)"/>
      <rect class="footer-stripe" x="0" y="967" width="908" height="16" fill="var(--sky-blue)"/>
      <rect class="footer-stripe" x="0" y="983" width="908" height="16" fill="var(--mid-blue)"/>
      <rect class="footer-band" x="0" y="999" width="908" height="176" fill="var(--navy)"/>
    </svg>

    <div class="brand-corner">KT<br>Fabrications</div>
    <div class="brand-wordmark">KT FABRICATIONS</div>
    <div class="brand-watermark">KT FABRICATIONS</div>

    <ul class="footer-address">
      <li>KT Fabrications Limited</li>
      <li>Hallmere Road</li>
      <li>Ashbridge</li>
      <li>Northmere</li>
      <li>LP47 9XZ, UK</li>
    </ul>

    <ul class="footer-contact">
      <li>+44 (0)1632 960418
        <svg viewBox="0 0 12 12" aria-label="Telephone"><path d="M3,1 L5,3.5 L4,5 Q5,7.5 7,8 L8.5,7 L11,9 L9.5,11 Q3,10 1,2.5 Z" fill="none" stroke="var(--sky-blue)" stroke-width="1"/></svg>
      </li>
      <li>+44 (0)1632 960733
        <svg viewBox="0 0 12 12" aria-label="Fax"><rect x="3" y="1" width="6" height="3.5" fill="none" stroke="var(--sky-blue)"/><rect x="1" y="4.5" width="10" height="4.5" rx="1" fill="none" stroke="var(--sky-blue)"/><rect x="3" y="7.5" width="6" height="3.5" fill="none" stroke="var(--sky-blue)"/></svg>
      </li>
      <li>sales@ktfabrications.example
        <svg viewBox="0 0 12 12" aria-label="Email"><circle cx="6" cy="6" r="2" fill="none" stroke="var(--sky-blue)" stroke-width="1.2"/><path d="M8,4 V7 Q8,9 10,8 Q11.5,6.5 11,5 A5,5 0 1 0 8.5,10.5" fill="none" stroke="var(--sky-blue)" stroke-width="1.2"/></svg>
      </li>
      <li>www.ktfabrications.example
        <svg viewBox="0 0 12 12" aria-label="Website"><circle cx="6" cy="6" r="5" fill="none" stroke="var(--sky-blue)"/><ellipse cx="6" cy="6" rx="2.2" ry="5" fill="none" stroke="var(--sky-blue)"/><path d="M1,6 H11 M2,3.5 H10 M2,8.5 H10" stroke="var(--sky-blue)" stroke-width="0.8"/></svg>
      </li>
    </ul>
  </main>
</body>
</html>
```